Business card and stationary designs for Harbor Summit Mentor
Harbor Summit Mentor
Business card and stationary designs for Harbor Summit Mentor - Consulting
Creative Brief
Professional
Reed Calloway
Executive & Professional Coach
4187 Willow Bend Lane Dallas TX 75231
RCalloway@harborsummitmentor.example
www.HarborSummitMentor.example
I want this to look clean, cutting edge, and for the design to stand out.
On the back of the business card I would like my logo and the phrase "Executive & Professional Coaching"

```html
<!DOCTYPE html>
<html lang="en">
<head>
<meta charset="utf-8">
<title>Harbor Summit Mentor – Stationery Set</title>
<link href="https://fonts.googleapis.com/css2?family=Cinzel:wght@400&family=Lato:wght@400&display=swap" rel="stylesheet">
<style>
:root{
  --backdrop:#9b9b9b;
  --paper:#ffffff;
  --ink:#111111;
  --muted:#6d6d6d;
  --faint:#ececec;
  --pocket:#8a8a8a;
  --pocket-dark:#777777;
  --rule:#c8c8c8;
}
*{box-sizing:border-box;margin:0;padding:0}
html,body{width:1200px;height:394px;overflow:hidden;background:var(--backdrop)}
.canvas{position:relative;width:1200px;height:394px}
.sheet{position:absolute;background:var(--paper);overflow:hidden}
.brand{font-family:'Cinzel',serif;color:var(--ink);letter-spacing:.04em;white-space:nowrap;line-height:1}
.brand-light{color:var(--paper)}
.mark{display:inline-block;width:5px;height:5px;background:currentColor;margin-right:3px;vertical-align:middle}
.small{font-family:'Lato',sans-serif;font-size:3.4px;color:var(--muted);line-height:1.4;white-space:nowrap}
.small-light{color:#d6d6d6}
.watermark{position:absolute;left:0;right:0;text-align:center;font-family:'Cinzel',serif;color:var(--faint);line-height:1.1}
.band{position:absolute;left:0;right:0;background:var(--ink)}
.center{position:absolute;left:0;right:0;text-align:center}

/* business cards */
.card{left:31px;width:79px;height:45px}
.card-front{top:106px}
.card-back{top:158px;background:var(--ink)}
.card-alt{top:211px}

/* letterheads */
.letterhead{top:43px;width:202px;height:317px}
.letterhead-main{left:127px}
.letterhead-fax{left:343px}
.footer-band{bottom:16px;height:9px}
.footer-grey{position:absolute;left:0;right:0;bottom:0;height:16px;background:var(--rule)}
.fax-title{position:absolute;left:18px;top:45px;font-family:'Lato',sans-serif;font-size:6px;color:var(--ink);letter-spacing:.1em}
.fax-table{position:absolute;left:18px;top:56px;width:166px;border-collapse:collapse;font-family:'Lato',sans-serif;font-size:3.4px;color:var(--muted)}
.fax-table td{border:0.5px solid var(--rule);height:9px;padding-left:2px}

/* envelope + slip */
.slip{left:559px;top:43px;width:211px;height:72px}
.envelope-front{left:559px;top:125px;width:211px;height:132px}
.envelope-back{left:559px;top:269px;width:211px;height:91px}

/* folder */
.folder{position:absolute;left:785px;top:43px;width:382px;height:317px}
.folder-cover{position:absolute;left:0;top:0;width:191px;height:317px;background:var(--ink)}
.folder-inside{position:absolute;left:191px;top:0;width:191px;height:317px;background:var(--paper)}
.pocket-left{position:absolute;left:0;bottom:0;width:191px;height:84px;background:var(--pocket)}
.pocket-right{position:absolute;left:191px;bottom:0;width:191px;height:84px;background:var(--pocket-dark)}
</style>
</head>
<body>
<main class="canvas">

  <!-- business cards -->
  <section class="sheet card card-front">
    <div class="brand" style="position:absolute;left:6px;top:8px;font-size:4.5px"><span class="mark"></span>Harbor Summit Mentor</div>
    <div class="small" style="position:absolute;left:6px;top:20px">
      Reed Calloway<br>Executive &amp; Professional Coach<br>RCalloway@harborsummitmentor.example
    </div>
  </section>
  <section class="sheet card card-back">
    <div class="center brand brand-light" style="top:15px;font-size:5.5px">Harbor Summit Mentor</div>
    <div class="center small small-light" style="top:26px">Executive &amp; Professional Coaching</div>
  </section>
  <section class="sheet card card-alt">
    <div class="center brand" style="top:18px;font-size:5px">Harbor Summit Mentor</div>
  </section>

  <!-- letterhead -->
  <section class="sheet letterhead letterhead-main">
    <div class="center brand" style="top:14px;font-size:6px"><span class="mark"></span>Harbor Summit Mentor</div>
    <div class="watermark" style="top:132px;font-size:15px">Harbor Summit<br>Mentor</div>
    <div class="band footer-band"></div>
    <div class="center small small-light" style="bottom:17px">4187 Willow Bend Lane Dallas TX 75231 · www.HarborSummitMentor.example</div>
    <div class="footer-grey"></div>
  </section>

  <!-- fax sheet -->
  <section class="sheet letterhead letterhead-fax">
    <div class="center brand" style="top:14px;font-size:6px"><span class="mark"></span>Harbor Summit Mentor</div>
    <div class="fax-title">FAX</div>
    <table class="fax-table">
      <tr><td>To</td><td>From</td></tr>
      <tr><td>Fax</td><td>Pages</td></tr>
      <tr><td>Date</td><td>Re</td></tr>
      <tr><td>Phone</td><td>CC</td></tr>
    </table>
    <div class="watermark" style="top:132px;font-size:15px">Harbor Summit<br>Mentor</div>
    <div class="band footer-band"></div>
    <div class="center small small-light" style="bottom:17px">4187 Willow Bend Lane Dallas TX 75231 · www.HarborSummitMentor.example</div>
    <div class="footer-grey"></div>
  </section>

  <!-- compliment slip -->
  <section class="sheet slip">
    <div class="brand" style="position:absolute;left:10px;top:10px;font-size:5px"><span class="mark"></span>Harbor Summit Mentor</div>
    <div class="band" style="top:52px;height:8px"></div>
    <div class="center small small-light" style="top:53px">www.HarborSummitMentor.example</div>
  </section>

  <!-- envelope front -->
  <section class="sheet envelope-front">
    <div class="brand" style="position:absolute;left:10px;top:10px;font-size:5px"><span class="mark"></span>Harbor Summit Mentor</div>
    <div class="small" style="position:absolute;left:10px;top:19px">4187 Willow Bend Lane Dallas TX 75231</div>
    <div class="band" style="bottom:12px;height:10px"></div>
    <div class="center small small-light" style="bottom:14px">www.HarborSummitMentor.example</div>
  </section>

  <!-- envelope back -->
  <section class="sheet envelope-back">
    <svg width="211" height="91" viewBox="0 0 211 91" aria-hidden="true">
      <path d="M0 0 H211 V14 L105.5 46 L0 14 Z" fill="#111111"/>
      <path d="M0 14 L105.5 46 L211 14" fill="none" stroke="#c8c8c8" stroke-width="0.6"/>
      <path d="M0 91 L105.5 52 L211 91" fill="none" stroke="#e0e0e0" stroke-width="0.6"/>
    </svg>
  </section>

  <!-- presentation folder -->
  <section class="folder">
    <div class="folder-cover">
      <div class="center brand brand-light" style="top:140px;font-size:10px">Harbor Summit<br>Mentor</div>
    </div>
    <div class="folder-inside">
      <div class="brand" style="position:absolute;left:60px;top:14px;font-size:7px"><span class="mark"></span>Harbor Summit Mentor</div>
      <div class="band" style="left:64px;top:192px;height:9px"></div>
      <div class="small small-light" style="position:absolute;left:70px;top:194px">www.HarborSummitMentor.example</div>
    </div>
    <div class="pocket-left">
      <div class="center small small-light" style="top:10px">4187 Willow Bend Lane Dallas TX 75231</div>
    </div>
    <div class="pocket-right"></div>
  </section>

</main>
</body>
</html>
```